Design for Torvel Ginger Chewy Candy!

Hello! We are Torvel Enterprises Corp, a food manufacturer and distributor based in Los Angeles, CA. We manufacture Chips, Cookies, Juices, Dairy, and last but not least, Candies! We are launching our Ginger Chewy Candy soon and we need a great design for it!

Our Ginger Chewy Candy is a perfect mixture between sweet and spicy from the ginger itself. Torvel Ginger Chewy Candy a good relief for sore throat and nausea.

Now, other than a great design, we also welcome brand suggestions for the candy.
If you can come up with a logo for the Ginger Candy, that would be swell!

We are open to unique and out of the box design. We chose a few color schemes for the design, but feel free to step out of the box if you feel it suits the brand.

We don't have the exact size for the plastic pouch, but it should be a generic small plastic pouch size (approximately 4 oz resealable plastic pouch)

Please have fun designing the project, we can't wait to see all the great designs!

Cheers!

Target Market(s)

USA and Asian market
Age 30-70
Male and Female

Industry/Entity Type

Manufacture

Font styles to use
Serif
Sans Serif
Decorative

Colors
fff3d1
fee18a
fece3e
fbc994
fce8d3

Requirements
Must have
• Torvel Logo
• A picture of ginger (illustrations or photographs are welcome)
Nice to have
• Coating suggestions like Matte surface or SPOT UV
• Give us ideas of what the name of the chewy candy should be. Product name ideas are welcome!

```html
<!DOCTYPE html>
<html lang="en">
<head>
<meta charset="utf-8">
<title>Torvel Zinglo Chew Ginger Candy – Pouch Front</title>
<link rel="stylesheet" href="https://fonts.googleapis.com/css2?family=Luckiest+Guy&family=Montserrat:wght@600;700&display=swap">
<style>
  :root {
    --cream: #fff3d1;
    --butter: #fee18a;
    --sun: #fece3e;
    --peach: #fbc994;
    --pale-peach: #fce8d3;
    --dot-field: #f6f0dc;
    --ink: #111111;
    --leaf-green: #1f4a1f;
    --brand-blue: #1e6fb3;
    --logo-navy: #2a2f7a;
    --white: #ffffff;
    --ginger-light: #e2c49a;
    --ginger-mid: #cfa672;
    --leaf-dark: #2f5a34;
  }
  html, body {
    margin: 0;
    padding: 0;
    overflow: hidden;
    background: var(--white);
  }
  .pouch-front {
    position: relative;
    width: 838px;
    height: 1200px;
    overflow: hidden;
    font-family: "Montserrat", Arial, sans-serif;
  }
  .pouch-art {
    position: absolute;
    inset: 0;
    display: block;
  }
  .brand-name {
    font-family: "Montserrat", Arial, sans-serif;
    font-weight: 700;
    font-size: 58px;
    fill: var(--logo-navy);
  }
  .claim {
    font-weight: 700;
    font-size: 36px;
    fill: var(--ink);
  }
  .descriptor {
    font-weight: 700;
    font-size: 42px;
    fill: var(--leaf-green);
  }
  .product-name {
    font-family: "Luckiest Guy", "Arial Black", sans-serif;
    font-size: 128px;
    fill: var(--white);
    stroke: var(--brand-blue);
    stroke-width: 16px;
    stroke-linejoin: round;
    paint-order: stroke;
  }
  .count {
    font-weight: 700;
    fill: var(--ink);
    font-size: 62px;
    letter-spacing: -2px;
  }
  .net-weight {
    font-weight: 700;
    font-size: 40px;
    fill: var(--ink);
  }
</style>
</head>
<body>
<main class="pouch-front">
  <svg class="pouch-art" width="838" height="1200" viewBox="0 0 838 1200" xmlns="http://www.w3.org/2000/svg">
    <defs>
      <linearGradient id="ginger-tones" x1="0" y1="0" x2="1" y2="1">
        <stop offset="0" stop-color="var(--leaf-dark)"/>
        <stop offset="0.3" stop-color="var(--ginger-light)"/>
        <stop offset="0.7" stop-color="var(--ginger-mid)"/>
        <stop offset="1" stop-color="var(--sun)"/>
      </linearGradient>
      <path id="name-arc" d="M50,805 Q330,635 815,592"/>
    </defs>

    <rect class="dot-field" x="0" y="54" width="838" height="1146" fill="var(--dot-field)" role="img" aria-label="Yellow and grey polka dot pattern on white"/>

    <rect class="top-band" x="0" y="0" width="838" height="27" fill="var(--butter)"/>
    <rect class="seal-band" x="0" y="27" width="838" height="27" fill="var(--peach)"/>

    <path class="ginger-photo" role="img" aria-label="Photograph of fresh ginger roots with sliced ginger and green leaves"
          d="M50,930 Q120,780 300,700 Q470,640 640,650 Q760,660 838,700 L838,1060 L50,1060 Z"
          fill="url(#ginger-tones)"/>

    <path class="name-band" d="M0,700 Q380,500 838,440 L838,605 Q560,625 340,760 Q170,860 70,960 L0,975 Z" fill="var(--sun)"/>
    <path class="band-rule" d="M312,748 Q540,625 838,606" fill="none" stroke="var(--brand-blue)" stroke-width="7" stroke-linecap="round"/>

    <path class="base-wave-edge" d="M0,925 Q210,885 420,945 Q640,1005 838,965 L838,1200 L0,1200 Z" fill="var(--butter)"/>
    <path class="base-wave" d="M0,945 Q210,905 420,965 Q640,1025 838,985 L838,1200 L0,1200 Z" fill="var(--sun)"/>

    <path class="brand-ribbon" d="M278,54 L566,54 L566,306 L422,230 L278,306 Z" fill="var(--sun)"/>
    <text class="brand-name" x="422" y="158" text-anchor="middle">Torvel</text>

    <text class="claim" x="246" y="352" textLength="366" lengthAdjust="spacing">100% NATURAL</text>
    <text class="descriptor" x="92" y="428" textLength="648" lengthAdjust="spacing">CHEW GINGER CANDY</text>

    <text class="product-name"><textPath href="#name-arc" textLength="740" lengthAdjust="spacingAndGlyphs">ZINGLO</textPath></text>

    <circle class="count-badge" cx="132" cy="1068" r="92" fill="var(--white)"/>
    <text class="count" x="122" y="1046" text-anchor="middle">50</text>
    <text class="count" x="136" y="1130" text-anchor="middle">PCS</text>

    <text class="net-weight" x="224" y="1152" textLength="580" lengthAdjust="spacing">NET WT/NETTO 100g</text>
  </svg>
</main>
</body>
</html>
```